Technology management company looking for a new website with a professional look

Brennick IT is a recently re-branded technology management company that is looking for a website design to match its personalized approach and friendly culture.

We would like to see a specialized, but related, page style for each of our main service offerings of:

• Commercial IT Support (This is our primary focus)
• Commercial Phone Systems (We partner with http://www.voxtrell.com/ for our phone systems)
• Point of Sale Systems (We partner with http://www.tillmora.com/ for our POS systems.
• Web Design
• Hollow Pine Computers (Our residential computer service offering, branded as Hollow Pine Computers)

The Hollow Pine Computers page should be build upon the Hollow Pine Computers logo, the other four pages should be branded as Brennick IT.

These five separate pages should have subtle, yet clearly defined links to one another. They should also each have a Home, Products, Service, and Company in the menu.

The website should have a clean design with professional appeal, but not appear too sterile or uninviting. It needs to have a simple, easy to navigate menu interface along the top. We would also like the site to be mobile friendly.

It should also allow us to easily tie in links to our social media pages (Facebook, LinkedIn, Twitter and Google+) and provide easy access to our contact information from each page.

This is a link to our old website www.hollowpinecomputers.com

We don't currently have copy available. The text and menu design should be easily editable and expandable so we can use the design to fit our copy.

In general we are looking for a concept we can modify to fit our needs.

We need this design to be available with layers in a .psd format.

Target Market(s)

Small to mid-size businesses.

Industry/Entity Type

Information Technology

Number of Pages Required

5+ page

Font styles to use
Sans Serif

Requirements
Must have
• Mobile Friendly
• Professional Type Face
• Unity between all pages
• .PSD Format
Nice to have
• Themed with our logo
Should not have
• Bubbly unprofessional typeface. No comic sans.

```html
<!DOCTYPE html>
<html lang="en">
<head>
<meta charset="utf-8">
<title>Brennick IT – Home</title>
<link rel="stylesheet" href="https://fonts.googleapis.com/css2?family=Raleway:wght@400;600;700;800&family=Open+Sans:wght@400;600;700&display=swap">
<style>
:root{
  --blue:#1e6fc6;
  --blue-dark:#0d3f86;
  --navy:#06163a;
  --red:#d8261f;
  --ink:#2b2f36;
  --muted:#777d86;
  --line:#e2e5ea;
  --gray-bg:#f1f2f4;
  --footer:#1d1f23;
  --footer-text:#a9adb4;
}
*{box-sizing:border-box;margin:0;padding:0}
html,body{width:1200px;height:2468px;overflow:hidden}
body{font-family:"Open Sans",Arial,sans-serif;color:var(--ink);background:#fff;font-size:13px;line-height:1.6}
h1,h2,h3,h4{font-family:"Raleway",Arial,sans-serif}
.wrap{width:1080px;margin:0 auto;position:relative}

/* header */
.site-header{height:56px;background:#fff;border-bottom:1px solid var(--line)}
.site-header .wrap{display:flex;align-items:center;height:56px}
.brand{display:flex;align-items:center;gap:10px;font-family:"Raleway",sans-serif;font-weight:800;font-size:19px;color:var(--blue-dark);text-transform:uppercase;letter-spacing:.5px}
.brand-mark{width:14px;height:14px;background:var(--blue);border-radius:50%}
.main-nav{margin-left:auto;display:flex;gap:34px;font-family:"Raleway",sans-serif;font-weight:700;font-size:12px;letter-spacing:.5px}
.main-nav a{color:var(--ink);text-decoration:none}
.header-actions{display:flex;gap:10px;margin-left:40px}
.btn-pill{font-family:"Raleway",sans-serif;font-weight:700;font-size:12px;color:#fff;padding:8px 16px;border-radius:3px;text-decoration:none}
.btn-portal{background:var(--blue)}
.btn-chat{background:var(--red)}

/* hero */
.hero{height:584px;position:relative;overflow:hidden;
  background:radial-gradient(ellipse 60% 55% at 50% 95%,#5db4ff 0%,#1b62c8 30%,transparent 70%),
  radial-gradient(ellipse 70% 60% at 50% 20%,#14408e 0%,transparent 70%),var(--navy)}
.hero-inner{position:absolute;top:240px;left:0;right:0;text-align:center;color:#fff}
.hero-kicker{font-family:"Raleway",sans-serif;font-weight:600;font-size:28px;letter-spacing:3px}
.hero-title{display:inline-block;margin-top:10px;border:3px solid #fff;padding:6px 36px;font-family:"Raleway",sans-serif;font-weight:600;font-size:52px;letter-spacing:2px;background:rgba(10,30,70,.35)}
.hero-dots{position:absolute;bottom:22px;left:0;right:0;display:flex;justify-content:center;gap:8px}
.hero-dots span{width:9px;height:9px;border-radius:50%;background:rgba(255,255,255,.5)}
.hero-dots span.on{background:#fff}

/* services */
.services{background:linear-gradient(#1d6bd0,#1558b6);height:360px;color:#fff}
.services .wrap{display:flex;justify-content:space-between;padding-top:46px}
.service{width:190px;text-align:center}
.service-icon{width:100px;height:100px;margin:0 auto 26px}
.service h3{font-size:14px;font-weight:800;line-height:1.3;text-transform:uppercase;letter-spacing:.3px}
.service p{font-size:11px;opacity:.85;margin:8px 0 16px;line-height:1.5}
.btn-more{display:inline-block;font-size:10px;font-weight:700;border:1px solid rgba(255,255,255,.8);padding:5px 16px;border-radius:2px;color:#fff;text-decoration:none}

/* welcome */
.welcome{height:432px;padding-top:62px}
.welcome .wrap{display:flex;gap:30px}
.section-title{font-size:16px;font-weight:800;text-transform:uppercase;letter-spacing:.3px;margin-bottom:16px}
.section-title em{font-style:normal;color:var(--blue)}
.welcome-copy{width:300px;color:var(--muted);font-size:12px}
.welcome-copy p{margin-bottom:12px}
.welcome-video{width:380px;height:260px;margin-top:40px;position:relative;background:linear-gradient(135deg,#4d5560,#23282f)}
.play{position:absolute;left:50%;top:50%;width:60px;height:60px;margin:-30px 0 0 -30px}
.why{flex:1}
.why ul{list-style:none}
.why li{display:flex;gap:10px;margin-bottom:18px}
.why li svg{flex:none;margin-top:3px}
.why strong{display:block;font-size:13px}
.why span{color:var(--muted);font-size:11px;line-height:1.5;display:block}

/* testimonials + blog */
.lower{background:var(--gray-bg);height:400px;padding-top:40px}
.lower .wrap{display:flex;gap:40px}
.testimonials{width:520px}
.quote-box{background:#fff;border:2px solid #9fc0ea;padding:28px 34px;font-style:italic;color:var(--muted);font-size:13px;line-height:1.7;height:170px}
.client{display:flex;align-items:center;gap:14px;margin-top:16px}
.client-photo{width:56px;height:56px;background:linear-gradient(#8e96a2,#5b636e)}
.client strong{display:block;font-size:13px}
.client span{font-size:11px;color:var(--muted)}
.blog{flex:1}
.post{display:flex;gap:14px;margin-bottom:18px}
.post-date{width:40px;text-align:center;flex:none;border:1px solid var(--line);background:#fff}
.post-date b{display:block;background:var(--blue);color:#fff;font-size:14px;line-height:22px}
.post-date i{font-style:normal;font-size:10px;color:var(--muted)}
.post h4{font-size:13px;font-weight:700}
.post p{font-size:11px;color:var(--muted);line-height:1.5}
.post p a{color:var(--blue);text-decoration:none}

/* solutions + partners */
.logos{height:236px;padding-top:36px}
.logos .wrap{display:flex;gap:40px}
.logo-group{flex:1}
.logo-row{display:flex;gap:14px}
.logo-tile{flex:1;height:90px;border:1px solid var(--line);display:flex;align-items:center;justify-content:center;font-family:"Open Sans",sans-serif;font-weight:700;font-size:17px;color:#3b4452}
.badge{width:80px;height:40px;background:#c9ced6}

/* newsletter */
.newsletter{background:var(--blue);height:72px}
.newsletter .wrap{display:flex;align-items:center;height:72px;gap:16px;color:#fff}
.newsletter h3{font-size:15px;font-weight:800;line-height:1.2;text-transform:uppercase;width:200px}
.field{margin-left:60px;width:240px;height:34px;background:#fff;border-radius:2px;color:#999;font-size:12px;padding:8px 12px}
.field + .field{margin-left:0}
.btn-send{background:var(--blue-dark);padding:8px 22px;font-weight:700;font-size:12px;border-radius:2px}

/* footer */
.site-footer{background:var(--footer);height:248px;color:var(--footer-text);font-size:11px;padding-top:32px}
.site-footer .wrap{display:flex;gap:50px}
.foot-col{width:230px}
.foot-col h4{color:#fff;font-size:13px;font-weight:800;text-transform:uppercase;margin-bottom:14px}
.foot-col p{margin-bottom:8px;line-height:1.5}
.foot-col b{color:#fff;font-weight:600}
.socials{display:flex;gap:8px;margin-bottom:14px}
.socials span{width:26px;height:26px;border:1px solid var(--footer-text);border-radius:50%}
</style>
</head>
<body>

<header class="site-header">
  <div class="wrap">
    <div class="brand"><span class="brand-mark"></span>Hollow Pine Computers</div>
    <nav class="main-nav"><a href="#">HOME</a><a href="#">PRODUCTS</a><a href="#">SERVICES</a><a href="#">COMPANY</a></nav>
    <div class="header-actions"><a class="btn-pill btn-portal" href="#">USER PORTAL</a><a class="btn-pill btn-chat" href="#">LIVE CHAT</a></div>
  </div>
</header>

<section class="hero" role="img" aria-label="Deep blue glowing digital network of light over a dark backdrop">
  <div class="hero-inner">
    <div class="hero-kicker">A CRYSTAL CLEAR</div>
    <div class="hero-title">PERSPECTIVE</div>
  </div>
  <div class="hero-dots"><span class="on"></span><span></span><span></span><span></span></div>
</section>

<section class="services">
  <div class="wrap">
    <div class="service">
      <svg class="service-icon" viewBox="0 0 100 100" fill="none" stroke="#fff" stroke-width="3"><rect x="20" y="20" width="60" height="60" rx="8" transform="rotate(45 50 50)"/><path d="M36 54v-6a14 14 0 0 1 28 0v6"/><rect x="33" y="52" width="7" height="12" rx="2"/><rect x="60" y="52" width="7" height="12" rx="2"/></svg>
      <h3>Commercial<br>IT Support</h3>
      <p>Lorem ipsum dolor sit amet, consectetur adipiscing elit.</p>
      <a class="btn-more" href="#">READ MORE</a>
    </div>
    <div class="service">
      <svg class="service-icon" viewBox="0 0 100 100" fill="none" stroke="#fff" stroke-width="3"><rect x="20" y="20" width="60" height="60" rx="8" transform="rotate(45 50 50)"/><rect x="36" y="38" width="28" height="26" rx="3"/><path d="M41 45h18M42 52h3M49 52h3M56 52h3M42 58h3M49 58h3M56 58h3"/></svg>
      <h3>Commercial<br>Phone Systems</h3>
      <p>Lorem ipsum dolor sit amet, consectetur adipiscing elit.</p>
      <a class="btn-more" href="#">READ MORE</a>
    </div>
    <div class="service">
      <svg class="service-icon" viewBox="0 0 100 100" fill="none" stroke="#fff" stroke-width="3"><rect x="20" y="20" width="60" height="60" rx="8" transform="rotate(45 50 50)"/><rect x="39" y="34" width="22" height="32" rx="2"/><path d="M44 42h12M44 48h12M44 54h12M44 60h6"/></svg>
      <h3>Point of<br>Sale Systems</h3>
      <p>Lorem ipsum dolor sit amet, consectetur adipiscing elit.</p>
      <a class="btn-more" href="#">READ MORE</a>
    </div>
    <div class="service">
      <svg class="service-icon" viewBox="0 0 100 100" fill="none" stroke="#fff" stroke-width="3"><rect x="20" y="20" width="60" height="60" rx="8" transform="rotate(45 50 50)"/><rect x="34" y="38" width="32" height="20" rx="2"/><path d="M44 64h12M50 58v6"/></svg>
      <h3>Web Design</h3>
      <p>Lorem ipsum dolor sit amet, consectetur adipiscing elit.</p>
      <a class="btn-more" href="#">READ MORE</a>
    </div>
    <div class="service">
      <svg class="service-icon" viewBox="0 0 100 100" fill="none" stroke="#fff" stroke-width="3"><rect x="20" y="20" width="60" height="60" rx="8" transform="rotate(45 50 50)"/><path d="M46 56l-4 4a6 6 0 0 1-8-8l6-6a6 6 0 0 1 8 0M54 44l4-4a6 6 0 0 1 8 8l-6 6a6 6 0 0 1-8 0M45 55l10-10"/></svg>
      <h3>Hollow Pine<br>Computers</h3>
      <p>Lorem ipsum dolor sit amet, consectetur adipiscing elit.</p>
      <a class="btn-more" href="#">READ MORE</a>
    </div>
  </div>
</section>

<section class="welcome">
  <div class="wrap">
    <div class="welcome-copy">
      <h2 class="section-title">Welcome to <em>Hollow Pine Computers</em></h2>
      <p>Hollow Pine Computers is a locally owned and operated full service computer solutions center.</p>
      <p>Our goal is to build a relationship with our clients, communicate clearly, and find timely, cost-effective solutions to your needs.</p>
      <p>From in-shop repair for personal computer systems to completely managed network solutions for our commercial clients, we deliver the service that best suits your unique requirements.</p>
    </div>
    <div class="welcome-video" role="img" aria-label="Video still of a technician working at a computer">
      <svg class="play" viewBox="0 0 60 60"><circle cx="30" cy="30" r="28" fill="rgba(0,0,0,.45)" stroke="#fff" stroke-width="2"/><path d="M24 18l18 12-18 12z" fill="#fff"/></svg>
    </div>
    <div class="why">
      <h2 class="section-title">Why Choose Us</h2>
      <ul>
        <li><svg width="14" height="14" viewBox="0 0 14 14"><circle cx="7" cy="7" r="7" fill="#1e6fc6"/><path d="M4 7l2 2 4-4" stroke="#fff" stroke-width="1.6" fill="none"/></svg><div><strong>Over 20 years of experience</strong><span>In publishing and graphic design, lorem document or visual presentation.</span></div></li>
        <li><svg width="14" height="14" viewBox="0 0 14 14"><circle cx="7" cy="7" r="7" fill="#1e6fc6"/><path d="M4 7l2 2 4-4" stroke="#fff" stroke-width="1.6" fill="none"/></svg><div><strong>We are passionate</strong><span>In publishing and graphic design, lorem document or visual presentation.</span></div></li>
        <li><svg width="14" height="14" viewBox="0 0 14 14"><circle cx="7" cy="7" r="7" fill="#1e6fc6"/><path d="M4 7l2 2 4-4" stroke="#fff" stroke-width="1.6" fill="none"/></svg><div><strong>We are fast, accuracy &amp; reliable</strong><span>In publishing and graphic design, lorem document or visual presentation.</span></div></li>
      </ul>
    </div>
  </div>
</section>

<section class="lower">
  <div class="wrap">
    <div class="testimonials">
      <h2 class="section-title">Client Testimonials</h2>
      <div class="quote-box">“Lorem ipsum dolor sit amet, consectetur adipiscing elit. Nam gravida metus ac lorem tincidunt, sit amet rhoncus nisi varius. Fusce dignissim eros vitae libero porta, vel feugiat justo pretium. Sed ut massa a nulla luctus facilisis.”</div>
      <div class="client">
        <div class="client-photo" role="img" aria-label="Client portrait"></div>
        <div><strong>Marla Quenby</strong><span>Lorem ipsum dolor sit</span></div>
      </div>
    </div>
    <div class="blog">
      <h2 class="section-title">Latest Blog</h2>
      <div class="post"><div class="post-date"><b>03</b><i>JUNE</i></div><div><h4>Lorem ipsum dolor sit amet...</h4><p>Lorem ipsum dolor sit amet gravida metus, tincidunt consectetur adipiscing elit nam... <a href="#">Read More</a></p></div></div>
      <div class="post"><div class="post-date"><b>01</b><i>JUNE</i></div><div><h4>Lorem ipsum dolor sit amet...</h4><p>Lorem ipsum dolor sit amet gravida metus, tincidunt consectetur adipiscing elit nam... <a href="#">Read More</a></p></div></div>
      <div class="post"><div class="post-date"><b>28</b><i>MAY</i></div><div><h4>Lorem ipsum dolor sit amet...</h4><p>Lorem ipsum dolor sit amet gravida metus, tincidunt consectetur adipiscing elit nam... <a href="#">Read More</a></p></div></div>
    </div>
  </div>
</section>

<section class="logos">
  <div class="wrap">
    <div class="logo-group">
      <h2 class="section-title">Solution for your tech needs</h2>
      <div class="logo-row"><div class="logo-tile">Fennix</div><div class="logo-tile">LinkDesk</div><div class="logo-tile">Remoto</div></div>
    </div>
    <div class="logo-group">
      <h2 class="section-title">Our Partners</h2>
      <div class="logo-row"><div class="logo-tile">Voxtrell</div><div class="logo-tile">Tillmora</div><div class="logo-tile"><span class="badge"></span></div></div>
    </div>
  </div>
</section>

<section class="newsletter">
  <div class="wrap">
    <svg width="40" height="40" viewBox="0 0 40 40" fill="none" stroke="#fff" stroke-width="2"><circle cx="20" cy="20" r="18"/><rect x="11" y="14" width="18" height="12"/><path d="M11 14l9 7 9-7"/></svg>
    <h3>Subscribe our newsletter</h3>
    <div class="field">Name</div>
    <div class="field">Email</div>
    <div class="btn-send">SEND</div>
  </div>
</section>

<footer class="site-footer">
  <div class="wrap">
    <div class="foot-col">
      <h4>Get in Touch</h4>
      <p>1820 Larch Rd. Suite 4<br>Millbrook, NY 12545</p>
      <p><b>Phone:</b><br>555-014-2288</p>
      <p><b>Email:</b><br>hello@hollowpinecomputers.com</p>
    </div>
    <div class="foot-col">
      <h4>Office Hours</h4>
      <p><b>Monday to Friday</b><br>8:00am – 5:00pm</p>
      <p><b>Saturday</b><br>9:00am – 12:00pm</p>
      <p><b>Sunday</b><br>Closed</p>
    </div>
    <div class="foot-col">
      <h4>Quick Links</h4>
      <p>Home</p><p>Products</p><p>Services</p><p>Company</p>
    </div>
    <div class="foot-col">
      <h4>Stay Connected</h4>
      <div class="socials"><span></span><span></span><span></span><span></span></div>
      <p>© 2015 Hollow Pine Computers.<br>All Rights Reserved. Terms &amp; Conditions.<br>Privacy Policy | Terms of Use</p>
    </div>
  </div>
</footer>

</body>
</html>
```